Harbour Lantern Fliers and logo design

We need to design a product logo and some informational fliers for a summit quest.
I have attached our Harbour Lantern logo - colours need to be complimentary but not the same, we would like fresh, funky but still professional. We generally communicate in a fairly casual way to reach our market. (We don't like boring)
Clear and simple - not too busy
images are good but not actual photos
Here is our website to give you an idea www.harbourlantern-example.co.nz
The flier is a 3 page document.
The logo is to say Summit Quest. The challenge is based on exercise, connecting with people, giving, learning and taking notice (The 4 keys to brightwater) Once agin the logo needs to be complementary but not the same.
The Harbour lantern logo needs to be on the fliers but the summit quest logo is separate.
Thanks very much!!

```html
<!DOCTYPE html>
<html lang="en">
<head>
<meta charset="utf-8">
<title>Harbour Lantern – Brochure Spread</title>
<link href="https://fonts.googleapis.com/css2?family=Archivo+Black&family=Cabin:wght@700&family=Roboto+Slab:wght@500&family=Open+Sans:wght@400;600&display=swap" rel="stylesheet">
<style>
  :root {
    --backdrop: #e6dfd9;
    --paper: #ffffff;
    --pattern-soft: #eef1f0;
    --pattern-mid: #dde3e1;
    --teal: #4fb89c;
    --teal-dark: #2f8a70;
    --ink: #1c1c1c;
    --parchment: #e6c184;
    --parchment-edge: #c99a55;
    --parchment-ink: #3a2a14;
    --title-band: #b07a35;
    --badge-red: #c8262f;
  }
  * { box-sizing: border-box; margin: 0; padding: 0; }
  html, body { width: 1200px; height: 824px; overflow: hidden; }
  body { background: var(--backdrop); font-family: "Open Sans", sans-serif; position: relative; }

  .spread { position: absolute; left: 60px; top: 30px; width: 1080px; height: 764px; display: flex; box-shadow: 0 10px 30px rgba(0,0,0,.12); }
  .page { position: relative; width: 540px; height: 764px; background: var(--paper); overflow: hidden; }
  .page--back { border-right: 1px solid #e4e4e4; }

  /* Icon pattern areas */
  .pattern-area { position: absolute; left: 0; right: 0; }
  .page--back .pattern-area { inset: 0; background: linear-gradient(180deg, var(--pattern-soft), var(--pattern-mid)); }
  .pattern-area--top { top: 0; height: 250px; background: linear-gradient(180deg, var(--pattern-mid), var(--pattern-soft)); }
  .pattern-area--bottom { bottom: 0; height: 130px; background: linear-gradient(180deg, var(--pattern-soft), var(--pattern-mid)); }

  /* Back page: tips */
  .tips-area { position: absolute; left: 60px; top: 90px; width: 420px; height: 610px; background: linear-gradient(180deg, var(--parchment-edge), var(--parchment) 10%, var(--parchment) 90%, var(--parchment-edge)); }
  .tips-content { position: absolute; left: 60px; top: 90px; width: 420px; height: 610px; }
  .tips-title { position: absolute; left: 36px; top: 34px; right: 36px; height: 42px; background: var(--title-band); color: #fff; font-family: "Cabin", sans-serif; font-weight: 700; font-size: 21px; display: flex; align-items: center; justify-content: center; }
  .tips-body { position: absolute; left: 36px; right: 34px; top: 98px; color: var(--parchment-ink); font-family: "Roboto Slab", serif; font-weight: 500; font-size: 11.5px; line-height: 1.5; }
  .tips-body p { margin-bottom: 12px; }
  .tips-list { list-style: none; }
  .tips-list li { position: relative; padding-left: 14px; margin-bottom: 8px; }
  .tips-list li::before { content: ""; position: absolute; left: 0; top: 6px; width: 6px; height: 6px; border-radius: 50%; background: var(--parchment-ink); }

  .quest-mark { position: absolute; display: flex; align-items: center; gap: 6px; font-family: "Open Sans", sans-serif; font-weight: 600; color: var(--ink); }
  .quest-mark__dot { border-radius: 50%; background: var(--badge-red); }
  .page--back .quest-mark { right: 76px; bottom: 86px; font-size: 11px; }
  .page--back .quest-mark__dot { width: 14px; height: 14px; }

  /* Cover */
  .cover-title { position: absolute; left: 60px; top: 285px; width: 430px; transform: rotate(-6deg); font-family: "Archivo Black", sans-serif; color: var(--ink); text-align: center; line-height: .95; }
  .cover-title__small { display: block; font-size: 30px; letter-spacing: 1px; }
  .cover-title__big { display: block; font-size: 66px; letter-spacing: -1px; }
  .cover-tagline { position: absolute; left: 40px; top: 420px; width: 460px; padding: 12px 30px; background: var(--teal); transform: rotate(-8deg); }
  .cover-tagline p { color: #fff; font-size: 10.5px; line-height: 1.4; text-align: center; }
  .brand-mark { position: absolute; left: 40px; bottom: 70px; display: flex; align-items: center; gap: 8px; font-family: "Open Sans", sans-serif; font-weight: 600; font-size: 16px; color: var(--teal-dark); }
  .brand-mark__dot { width: 18px; height: 18px; border-radius: 50%; background: var(--teal); }
  .page--cover .quest-mark { right: 44px; bottom: 170px; font-size: 15px; }
  .page--cover .quest-mark__dot { width: 30px; height: 30px; }
</style>
</head>
<body>
<main class="spread">
  <section class="page page--back">
    <div class="pattern-area" role="img" aria-label="Honeycomb pattern of faint wellbeing icons: hearts, smiles, runners, briefcases"></div>
    <div class="tips-area" role="img" aria-label="Parchment scroll illustration holding the tips list"></div>
    <div class="tips-content">
      <h2 class="tips-title">10 tips to improve your wellbeing</h2>
      <div class="tips-body">
        <p>Yes, you will have to get off the couch, but small changes every day can make a huge difference.</p>
        <ul class="tips-list">
          <li>Put on your wake up grin – smile and think happy thoughts first thing.</li>
          <li>Drink water all day – it flushes out toxins and keeps your mind clear.</li>
          <li>Get active – take the stairs and walk at lunch to lift your energy.</li>
          <li>Eat a banana – a natural pick-me-up that helps you feel calm.</li>
          <li>Take notice – go outside and enjoy the sky, the trees and the breeze.</li>
          <li>Connect – call a friend or share a coffee with a colleague today.</li>
          <li>Play music – create a playlist that gets your happy hormones flowing.</li>
          <li>Remove a poison – swap one unhealthy habit for something better.</li>
          <li>Give – do something kind for someone else and notice how it feels.</li>
          <li>Keep learning – try something new every day to keep the cogs turning.</li>
        </ul>
      </div>
    </div>
    <div class="quest-mark"><span class="quest-mark__dot"></span>Summit Quest</div>
  </section>

  <section class="page page--cover">
    <div class="pattern-area pattern-area--top" role="img" aria-label="Honeycomb pattern of wellbeing icons: hearts, smiles, runners, briefcases, money bags"></div>
    <div class="pattern-area pattern-area--bottom" role="img" aria-label="Faint honeycomb pattern of wellbeing icons"></div>
    <h1 class="cover-title">
      <span class="cover-title__small">HARBOUR</span>
      <span class="cover-title__big">LANTERN</span>
    </h1>
    <div class="cover-tagline">
      <p>Programmes, initiatives and events developed to optimise wellbeing, personal development, workplace culture, job satisfaction, engagement, organisational commitment and to assist with change management.</p>
    </div>
    <div class="brand-mark"><span class="brand-mark__dot"></span>harbour lantern</div>
    <div class="quest-mark"><span class="quest-mark__dot"></span>Summit Quest</div>
  </section>
</main>
</body>
</html>
```